Flyer-Design für Logistikdienstleister
Zielgruppe
Logistikdienstleister
Aufgabenstellung
Modern, Innovativ, Dienstleister, Kreativ, Automobil, Mittelstand

```html
<!DOCTYPE html>
<html lang="de">
<head>
<meta charset="utf-8">
<title>StockHarbor – Produktspektrum &amp; PSA-Aktion 2020</title>
<link rel="stylesheet" href="https://fonts.googleapis.com/css2?family=Open+Sans:wght@300;400;600;700&display=swap">
<style>
  :root {
    --canvas-bg: #f2f2f2;
    --page-bg: #ffffff;
    --brand-red: #cf0f23;
    --text-gray: #5f5f5f;
    --body-gray: #555555;
    --teal: #25b3b0;
    --ppe-blue: #3aa7d8;
    --white: #ffffff;
    --tile: rgba(255, 255, 255, 0.13);
  }
  * { box-sizing: border-box; margin: 0; padding: 0; }
  html, body { width: 1200px; height: 882px; overflow: hidden; }
  body {
    background: var(--canvas-bg);
    font-family: "Open Sans", Arial, sans-serif;
    position: relative;
  }
  .spread {
    position: absolute; left: 75px; top: 70px;
    width: 1052px; height: 746px; display: flex;
  }
  .page {
    position: relative; width: 526px; height: 746px;
    background: var(--page-bg); overflow: hidden;
  }
  .red-field { position: absolute; left: 0; top: 0; width: 526px; height: 746px; }
  .tile { position: absolute; background: var(--tile); }
  .tile-frame { position: absolute; border: 21px solid var(--tile); }

  /* left page */
  .kicker { position: absolute; font-weight: 400; font-size: 15px; color: var(--text-gray); }
  .left .kicker { left: 43px; top: 33px; }
  .headline {
    position: absolute; left: 43px; top: 52px;
    font-size: 30px; font-weight: 600; line-height: 1.08; color: var(--text-gray);
  }
  .intro {
    position: absolute; left: 43px; top: 141px; width: 370px;
    font-size: 10.2px; line-height: 15px; color: var(--body-gray);
    hyphens: auto;
  }
  .industries { position: absolute; left: 36px; top: 250px; color: var(--white); }
  .industries h2 { font-size: 15px; font-weight: 700; margin-bottom: 12px; }
  .industries p { font-size: 11.4px; line-height: 17.6px; }
  .benefit {
    position: absolute; top: 394px; width: 92px; margin-left: -46px;
    text-align: center; color: var(--white);
  }
  .benefit svg { width: 32px; height: 32px; display: block; margin: 0 auto 5px; }
  .benefit span { display: block; font-size: 5.4px; line-height: 1.35; }
  .photo { position: absolute; top: 476px; height: 225px; }
  .photo-lockers {
    left: 0; width: 261px;
    background:
      linear-gradient(100deg, rgba(30,34,48,0) 45%, rgba(30,34,48,0.92) 62%, rgba(30,34,48,0.9) 80%, rgba(150,152,158,0.7) 100%),
      linear-gradient(160deg, #b8bbc0 0%, #8a8d93 40%, #6c6f76 100%);
  }
  .photo-terminal {
    left: 265px; width: 261px;
    background:
      radial-gradient(ellipse 75% 70% at 62% 48%, #e6e7ea 0%, #c9cbd0 45%, rgba(40,40,44,0) 75%),
      linear-gradient(180deg, #1a1a1d 0%, #2b2b30 100%);
  }

  /* right page */
  .right .kicker { left: 0; width: 100%; top: 33px; text-align: center; }
  .event-title {
    position: absolute; left: 0; width: 100%; top: 50px; text-align: center;
    font-size: 32px; font-weight: 600; color: var(--text-gray);
  }
  .event-lead {
    position: absolute; left: 28px; width: 470px; top: 98px; text-align: center;
    font-size: 10.2px; line-height: 15px; color: var(--body-gray); hyphens: auto;
  }
  .ppe-panel {
    position: absolute; left: 65px; top: 165px; width: 395px; height: 297px;
    background: var(--teal);
  }
  .ppe-item {
    position: absolute; width: 84px; margin-left: -42px;
    text-align: center; color: var(--white); font-size: 8px; line-height: 1.3;
  }
  .ppe-item i {
    display: block; width: 58px; height: 58px; margin: 0 auto 6px;
    border-radius: 50%;
    background: radial-gradient(circle at 50% 52%, #8fcfe9 0%, #cfeaf5 38%, #ffffff 62%);
  }
  .ppe-suit {
    position: absolute; left: 270px; top: 10px; width: 94px; height: 242px;
    border-radius: 42px 42px 14px 14px;
    background: linear-gradient(90deg, #e7eef1 0%, #ffffff 30%, #ffffff 62%, #dbe8ed 100%);
  }
  .ppe-suit-label {
    position: absolute; left: 240px; top: 259px; width: 154px;
    text-align: center; color: var(--white); font-size: 8px; line-height: 1.4;
  }
  .event-copy {
    position: absolute; left: 20px; width: 486px; top: 516px; text-align: center;
    color: var(--white); font-size: 10.5px; line-height: 16.5px;
  }
  .event-copy p + p { margin-top: 19px; }
</style>
</head>
<body>
<main class="spread">

  <section class="page left">
    <svg class="red-field" viewBox="0 0 526 746" aria-hidden="true">
      <polygon points="0,213 526,272 526,746 0,746" fill="var(--brand-red)"/>
    </svg>
    <div class="tile" style="left:265px;top:247px;width:22px;height:227px"></div>
    <div class="tile" style="left:312px;top:271px;width:84px;height:85px"></div>
    <div class="tile" style="left:419px;top:271px;width:84px;height:85px"></div>
    <div class="tile" style="left:312px;top:377px;width:84px;height:88px"></div>
    <div class="tile" style="left:419px;top:377px;width:84px;height:88px"></div>

    <p class="kicker">Produktspektrum:</p>
    <h1 class="headline">optimierte supply chain<br>für alle Anwendungen</h1>
    <p class="intro">StockHarbor unterstützt Organisationen und Unternehmen weltweit. Besondere Schwerpunkte sind MRO (Maintenance, Repair and Operations), PPE (Personal Protection Equipment) sowie cutting tools. Dabei wird eine große Anzahl von Branchen bedient.</p>

    <div class="industries">
      <h2>Industries</h2>
      <p>Aerospace | Asset Management<br>Automotive | Rail | Lab &amp; Medical | Government<br>Office supplies | Maintenance &amp; Workshops | Process Industries<br>Industrial Manufacturing</p>
    </div>

    <div class="benefit" style="left:57px">
      <svg viewBox="0 0 36 36" fill="none" stroke="#fff" stroke-width="2"><path d="M4 10V4h6M26 4h6v6M32 26v6h-6M10 32H4v-6"/><rect x="9" y="10" width="18" height="16"/></svg>
      <span>Senkung der Lagerkosten<br>und Erhöhung des Kapitals</span>
    </div>
    <div class="benefit" style="left:146px">
      <svg viewBox="0 0 36 36" fill="#fff"><rect x="6" y="8" width="6" height="22"/><rect x="15" y="16" width="6" height="14"/><rect x="24" y="22" width="6" height="8"/><path d="M6 4l24 16" stroke="#fff" stroke-width="2"/><rect x="3" y="31" width="30" height="2"/></svg>
      <span>Reduzierung des<br>Verbrauchs um 25-40%</span>
    </div>
    <div class="benefit" style="left:236px">
      <svg viewBox="0 0 36 36" fill="none" stroke="#fff" stroke-width="2.4"><path d="M30 18a12 12 0 1 1-4-9"/><path d="M27 4v6h-6"/><text x="18" y="21" fill="#fff" stroke="none" font-size="9" font-weight="700" text-anchor="middle" font-family="Open Sans, sans-serif">24/7</text></svg>
      <span>Bereitstellung der 24 / 7-<br>Verfügbarkeit von Produkten</span>
    </div>
    <div class="benefit" style="left:340px">
      <svg viewBox="0 0 36 36" fill="none" stroke="#fff" stroke-width="2"><path d="M7 3h15l6 6v22H7z"/><path d="M11 11h10M11 16h12M11 21h8"/><rect x="17" y="24" width="16" height="9" fill="#fff"/></svg>
      <span>Bietet einen Nachweis<br>über die ausgegebenen Artikel</span>
    </div>
    <div class="benefit" style="left:427px">
      <svg viewBox="0 0 36 36" fill="none" stroke="#fff" stroke-width="2"><circle cx="10" cy="10" r="7"/><path d="M10 6v4h3"/><circle cx="24" cy="10" r="3" fill="#fff"/><path d="M20 15h8v9h-2v9h-4v-9h-2z" fill="#fff"/></svg>
      <span>Reduzierung der Wege-<br>und Wartezeiten</span>
    </div>

    <div class="photo photo-lockers" role="img" aria-label="Foto: Hand öffnet ein Fach eines Ausgabeautomaten mit vielen Metallschubladen"></div>
    <div class="photo photo-terminal" role="img" aria-label="Foto: Finger tippt auf den Touchscreen eines Ausgabeterminals"></div>
  </section>

  <section class="page right">
    <svg class="red-field" viewBox="0 0 526 746" aria-hidden="true">
      <polygon points="0,278 526,338 526,746 0,746" fill="var(--brand-red)"/>
    </svg>
    <div class="tile" style="left:0;top:278px;width:84px;height:83px"></div>
    <div class="tile" style="left:0;top:381px;width:84px;height:88px"></div>
    <div class="tile" style="left:0;top:489px;width:84px;height:88px"></div>
    <div class="tile-frame" style="left:-40px;top:400px;width:170px;height:221px"></div>

    <p class="kicker">Persönliche Schutzausrüstungen:</p>
    <h1 class="event-title">PSA-Aktion 2020</h1>
    <p class="event-lead">Verwalten Sie Ihren PSA-Bestand in sicherer Art und Weise, von Ihrem Büro aus!<br>In der aktuellen Lage ist es wichtiger denn je, PSA-Vorräte vernünftig zu organisie-<br>ren und auszugeben.</p>

    <div class="ppe-panel">
      <div class="ppe-item" style="left:53px;top:20px"><i role="img" aria-label="Illustration: Schutzbrille"></i>Goggles</div>
      <div class="ppe-item" style="left:132px;top:20px"><i role="img" aria-label="Illustration: Gesichtsschild"></i>Face Shield</div>
      <div class="ppe-item" style="left:210px;top:20px"><i role="img" aria-label="Illustration: OP-Haube"></i>Medical Cap</div>
      <div class="ppe-item" style="left:53px;top:103px"><i role="img" aria-label="Illustration: OP-Maske"></i>Surgical Mask</div>
      <div class="ppe-item" style="left:132px;top:103px"><i role="img" aria-label="Illustration: FFP2-Maske"></i>N95 Mask</div>
      <div class="ppe-item" style="left:210px;top:103px"><i role="img" aria-label="Illustration: Überschuhe"></i>Shoes Cover</div>
      <div class="ppe-item" style="left:53px;top:192px"><i role="img" aria-label="Illustration: Desinfektionsgel und -spray"></i>Alcohol Gel<br>Alcohol Spray</div>
      <div class="ppe-item" style="left:132px;top:192px"><i role="img" aria-label="Illustration: Einweghandschuhe"></i>Disposable Gloves</div>
      <div class="ppe-item" style="left:210px;top:192px"><i role="img" aria-label="Illustration: Beinschutz"></i>Leg Cover</div>
      <div class="ppe-suit" role="img" aria-label="Illustration: weißer Schutzanzug mit Kapuze und blauen Nähten"></div>
      <p class="ppe-suit-label">Personal Protective Equipment<br>( PPE )</p>
    </div>

    <div class="event-copy">
      <p>Die Bestandsverwaltung von PSA Artikeln mit StockHarbor könnte<br>einfacher nicht sein!</p>
      <p>Es ist wichtig, allen Mitarbeitern die erforderliche Schutzausrüstung zur Verfügung<br>zu stellen, damit sie ihre Arbeit sicher ausführen können.</p>
      <p>Unsere Ausgabeautomaten können hierzu zentral an einem Standort<br>platziert oder vernetzt über das gesamte Firmengelände verteilt werden.</p>
    </div>
  </section>

</main>
</body>
</html>
```